Corporate Two Sided Business Card

Looking for a Corporate "edgy" Modern look and feel for a business card

We are looking at two options. Dark background with our logo on it, white background with our logo on it - The background is more - Charcoal / Graphite then black

Details will be

Rosalind Tebb

Licensee / Director

m. 0452 918 604

e. rosalind@quarvelhome.com.au

quarvelhome.com.au

Target Market(s)

Professional Business people that refer use business and clients that own Investment Properties

Industry/Entity Type

Business

Contact Information for Business Card

Details will be

Rosalind Tebb

Licensee / Director

m. 0452 918 604

quarvelhome.com.au

Font styles to use
Serif

Colors
000000
ec1f27
eeeeee
ffffff

Requirements
Must have
• Two options - White Background and Dark Background. - Two sided
Nice to have
• A design that is edgy, modern and new to look instead of boring style corporate cards - It should be a full integrated design
Should not have
• Block looking - Cheap.

```html
<!DOCTYPE html>
<html lang="en">
<head>
<meta charset="utf-8">
<title>Quarvelhome Business Card</title>
<link href="https://fonts.googleapis.com/css2?family=Poppins:wght@600&family=Questrial&display=swap" rel="stylesheet">
<style>
  :root {
    --stage: #2a2a2a;
    --graphite: #1f1f1f;
    --graphite-edge: #2c2c2c;
    --red: #ec1f27;
    --white: #eeeeee;
    --soft: #cfcfcf;
  }
  * { margin: 0; padding: 0; box-sizing: border-box; }
  html, body { width: 1200px; height: 834px; overflow: hidden; }
  body {
    background: var(--stage);
    display: flex;
    align-items: center;
    justify-content: center;
    gap: 40px;
    font-family: "Questrial", sans-serif;
  }
  .card {
    position: relative;
    width: 540px;
    height: 330px;
    background: var(--graphite);
    border: 1px solid var(--graphite-edge);
    box-shadow: 0 18px 40px rgba(0,0,0,0.45);
    color: var(--white);
  }
  .brand {
    display: flex;
    align-items: center;
    gap: 10px;
    font-family: "Poppins", sans-serif;
    font-weight: 600;
    color: var(--white);
    letter-spacing: 0.5px;
  }
  .brand-mark {
    width: 14px;
    height: 14px;
    background: var(--red);
  }
  .card-front .brand {
    position: absolute;
    left: 0; right: 0; top: 118px;
    justify-content: center;
    font-size: 44px;
  }
  .card-front .web {
    position: absolute;
    left: 0; right: 0; top: 238px;
    text-align: center;
    font-size: 13px;
    color: var(--white);
  }
  .web .accent { color: var(--red); }
  .card-back .brand {
    position: absolute;
    left: 36px; top: 150px;
    font-size: 34px;
  }
  .details {
    position: absolute;
    left: 318px; top: 92px;
  }
  .details .name {
    font-family: "Poppins", sans-serif;
    font-weight: 600;
    font-size: 15px;
    color: var(--white);
  }
  .details .role {
    font-size: 12px;
    color: var(--red);
    margin-top: 2px;
  }
  .contacts {
    list-style: none;
    margin-top: 18px;
  }
  .contacts li {
    display: flex;
    align-items: center;
    gap: 10px;
    font-size: 12px;
    color: var(--soft);
    margin-bottom: 9px;
  }
  .contacts svg { width: 13px; height: 13px; flex: none; }
</style>
</head>
<body>
  <section class="card card-front">
    <div class="brand"><span class="brand-mark"></span>quarvelhome</div>
    <p class="web"><span class="accent">www.</span>quarvelhome<span class="accent">.com.au</span></p>
  </section>

  <section class="card card-back">
    <div class="brand"><span class="brand-mark"></span>quarvelhome</div>
    <div class="details">
      <p class="name">Rosalind Tebb</p>
      <p class="role">Licensee / Director</p>
      <ul class="contacts">
        <li>
          <svg viewBox="0 0 16 16" aria-hidden="true"><path d="M2 6c0-2 3-3 6-3s6 1 6 3v1h-3V5.5C10 5 9 5 8 5s-2 0-3 .5V7H2z M4 8h8l1 5H3z" fill="var(--red)"/></svg>
          0452 918 604
        </li>
        <li>
          <svg viewBox="0 0 16 16" aria-hidden="true"><rect x="1.5" y="3.5" width="13" height="9" fill="none" stroke="var(--red)" stroke-width="1.5"/><path d="M1.5 3.5 8 9l6.5-5.5" fill="none" stroke="var(--red)" stroke-width="1.5"/></svg>
          rosalind@quarvelhome.com.au
        </li>
        <li>
          <svg viewBox="0 0 16 16" aria-hidden="true"><circle cx="8" cy="8" r="6.5" fill="none" stroke="var(--red)" stroke-width="1.5"/><ellipse cx="8" cy="8" rx="2.8" ry="6.5" fill="none" stroke="var(--red)" stroke-width="1.2"/><path d="M1.5 8h13" stroke="var(--red)" stroke-width="1.2"/></svg>
          www.quarvelhome.com.au
        </li>
      </ul>
    </div>
  </section>
</body>
</html>
```